Private Investigation Business Card Design

I need a business card for a new private investigation company named Brisk Lens Inquiries. I perform mainly surveillance jobs, vehicle repossessions, document serves etc. The final design should aim for a professional look. The logo has a magnifying glass with stick man arms and legs and is in a running action to show the "BRISK" aspect of the name. If the colour scheme could remain the same as the website www.brisklensinquiries.example.au with silvers,blacks and a couple electric blue highlights.
Industry/Entity Type
Business
Contact Information for Business Card
Morgan Kilbride
Brisk Lens Inquiries
0438276104
PO Box 58, Fernvale NSW 2291
info@brisklensinquiries.example.au
www.brisklensinquiries.example.au
Look and feel
Each slider illustrates characteristics of the customer's brand and the style your logo design should communicate.

```html
<!DOCTYPE html>
<html lang="en">
<head>
<meta charset="utf-8">
<title>Brisk Lens Inquiries – Business Card</title>
<link href="https://fonts.googleapis.com/css2?family=Lato:wght@400;700;900&display=swap" rel="stylesheet">
<style>
  :root {
    --page-bg: #dcd7d0;
    --card-light: #f5f4f2;
    --card-mid: #e6e4e1;
    --card-edge: #c9c6c1;
    --ink: #3b3b3b;
    --ink-soft: #4a4a4a;
    --band-dark: #3e3e3e;
    --band-mid: #8a8a8a;
    --band-light: #b9b9b9;
    --mark-grey: #555555;
  }
  * { margin: 0; padding: 0; box-sizing: border-box; }
  html, body {
    width: 1200px; height: 970px; overflow: hidden;
    background: var(--page-bg);
    font-family: "Lato", Arial, sans-serif;
  }
  .canvas { position: relative; width: 1200px; height: 970px; }
  .business-card {
    position: absolute;
    left: 172px; top: 247px;
    width: 855px; height: 475px;
    transform: scale(1.12);
    transform-origin: center;
    border-radius: 14px;
    background: linear-gradient(160deg, var(--card-light) 0%, var(--card-mid) 100%);
    border: 1px solid var(--card-edge);
    box-shadow: 0 10px 30px rgba(0,0,0,0.18);
    overflow: hidden;
    color: var(--ink);
  }
  .swoosh { position: absolute; inset: 0; width: 855px; height: 475px; }
  .brand {
    position: absolute; right: 62px; top: 58px;
    display: flex; align-items: center; gap: 18px;
  }
  .brand-name {
    font-weight: 900; font-size: 32px; letter-spacing: 1px;
    color: var(--mark-grey);
  }
  .brand-dot {
    width: 58px; height: 58px; border-radius: 50%;
    background: var(--mark-grey);
  }
  .person { position: absolute; left: 42px; top: 250px; }
  .person-name { font-weight: 700; font-size: 33px; line-height: 1.1; color: var(--ink); }
  .person-role { font-size: 22px; margin-top: 4px; color: var(--ink-soft); }
  .contact-list {
    position: absolute; left: 42px; top: 354px;
    list-style: none; font-size: 20px; line-height: 25px; color: var(--ink);
  }
  .contact-list li { display: flex; align-items: center; gap: 10px; }
  .contact-icon { width: 22px; height: 18px; flex: none; }
  .postal-address {
    position: absolute; right: 135px; top: 380px;
    text-align: right; font-size: 20px; line-height: 25px;
    font-style: normal; color: var(--ink);
  }
</style>
</head>
<body>
<main class="canvas">
  <section class="business-card">
    <svg class="swoosh" viewBox="0 0 855 475" aria-hidden="true">
      <defs>
        <linearGradient id="bandDark" x1="0" y1="0" x2="1" y2="0">
          <stop offset="0" stop-color="var(--band-dark)"/>
          <stop offset="0.5" stop-color="#5a5a5a"/>
          <stop offset="1" stop-color="var(--band-dark)"/>
        </linearGradient>
        <linearGradient id="bandLight" x1="0" y1="0" x2="1" y2="0">
          <stop offset="0" stop-color="var(--band-light)"/>
          <stop offset="1" stop-color="var(--band-mid)"/>
        </linearGradient>
      </defs>
      <path d="M0,128 C300,100 650,230 852,472 C620,262 320,176 0,178 Z" fill="url(#bandDark)"/>
      <path d="M0,180 C320,178 620,264 852,472 C600,282 320,196 0,200 Z" fill="url(#bandLight)"/>
    </svg>

    <div class="brand">
      <span class="brand-name">BRISK LENS INQUIRIES</span>
      <span class="brand-dot"></span>
    </div>

    <div class="person">
      <h1 class="person-name">Morgan Kilbride</h1>
      <p class="person-role">Director</p>
    </div>

    <ul class="contact-list">
      <li>
        <svg class="contact-icon" viewBox="0 0 22 18" aria-hidden="true">
          <path d="M2,7 Q11,0 20,7 L17,8 L15,5 L7,5 L5,8 Z" fill="var(--ink)"/>
          <rect x="4" y="9" width="14" height="8" rx="1.5" fill="var(--ink)"/>
        </svg>
        <span>0438276104</span>
      </li>
      <li>
        <svg class="contact-icon" viewBox="0 0 22 18" aria-hidden="true">
          <rect x="1.5" y="2.5" width="19" height="13" fill="none" stroke="var(--ink)" stroke-width="1.8"/>
          <path d="M1.5,2.5 L11,10 L20.5,2.5" fill="none" stroke="var(--ink)" stroke-width="1.8"/>
        </svg>
        <span>info@brisklensinquiries.example.au</span>
      </li>
      <li>
        <svg class="contact-icon" viewBox="0 0 22 18" aria-hidden="true">
          <rect x="2" y="1.5" width="18" height="11.5" fill="none" stroke="var(--ink)" stroke-width="1.8"/>
          <rect x="7" y="15" width="8" height="2" fill="var(--ink)"/>
        </svg>
        <span>www.brisklensinquiries.example.au</span>
      </li>
    </ul>

    <address class="postal-address">
      PO Box 58<br>
      Fernvale NSW 2291
    </address>
  </section>
</main>
</body>
</html>
```